Cool Simple Design for Baby Product

Our company is Tovarin. We need a package design for our cupboard lock product. We want to appear as caring, warm and close to earth company that aims to improve family life.

Logo is our company logo, colour can be changed if you feel the need for it. Pics 1 and 2 are of the product itself. Pics 3 to 6 are examples of packages and visuals that I do like very much, maybe something along those lines.

Pics 7 and 8 a re just examples of something that I do NOT like. They feel too busy and detailed.

UPDATE: Colourbox1 is the main file that you should work on, colourbox2 is sample of the suppliers default look, so you can see how it looks when it is assembled.

There will be little text, but not much, ALSO there will be text in Germany so please consider this when creating the design. It is not yet finalized what text there will be but something like this:

"Text1: This is English text and there will not be much more than these characters, but also there will be German translation in this same space"

"Text2: Maybe this text too, overall 300 English characters maximum on whole package and that's it"

Industry/Entity Type

Baby

Font styles to use
Decorative
Script

Requirements
Must have
• Simple, soothing, cool, valuable.
Nice to have
• Less is more.
Should not have
• Aggressive with lot of details and too much stuff.

```html
<!DOCTYPE html>
<html lang="en">
<head>
<meta charset="utf-8">
<title>Tovarin Cupboard Lock – Mailer Box Dieline</title>
<link href="https://fonts.googleapis.com/css2?family=Dancing+Script:wght@400;600;700&display=swap" rel="stylesheet">
<style>
  :root {
    --tone-top: #d3a9d1;
    --tone-mid: #afb1dc;
    --tone-bottom: #8dbce8;
    --cut-line: #1b1b22;
    --band: #ffffff;
    --ink-light: #ffffff;
    --brand-ink: #b08cc6;
  }
  html, body {
    margin: 0;
    padding: 0;
    width: 1200px;
    height: 1200px;
    overflow: hidden;
    background: #ffffff;
  }
  .dieline {
    display: block;
    width: 1200px;
    height: 1200px;
  }
  .panel-outline use { fill: none; stroke: var(--cut-line); stroke-width: 3; }
  .panel-fill use { fill: url(#boxTone); stroke: none; }
  .fold { stroke: var(--cut-line); stroke-width: 1.6; stroke-dasharray: 22 9; fill: none; }
  .crease { stroke: var(--cut-line); stroke-width: 1.6; fill: none; }
  .slot { fill: none; stroke: var(--cut-line); stroke-width: 1.6; }
  .band { fill: var(--band); }
  .band-dots { stroke: var(--band); stroke-width: 5; stroke-linecap: round; stroke-dasharray: 0 11; fill: none; }
  .script {
    font-family: 'Dancing Script', cursive;
    fill: var(--ink-light);
  }
  .product-title { font-size: 54px; font-weight: 700; }
  .tagline { font-size: 26px; font-weight: 600; }
  .brand-name { font-size: 46px; font-weight: 600; fill: var(--brand-ink); }
  .front-copy { font-size: 20px; }
  .front-copy-de { font-size: 20px; }
  .install-heading { font-size: 15px; font-weight: 600; text-decoration: underline; }
  .install-en { font-size: 16px; }
  .install-de { font-size: 14px; }
  .rule { stroke: var(--ink-light); stroke-width: 2; }
  .column-divider { stroke: var(--ink-light); stroke-width: 1; }
</style>
</head>
<body>
<svg class="dieline" viewBox="0 0 1500 1500" xmlns="http://www.w3.org/2000/svg">
  <defs>
    <linearGradient id="boxTone" gradientUnits="userSpaceOnUse" x1="0" y1="20" x2="0" y2="1480">
      <stop offset="0" stop-color="var(--tone-top)"/>
      <stop offset="0.5" stop-color="var(--tone-mid)"/>
      <stop offset="1" stop-color="var(--tone-bottom)"/>
    </linearGradient>

    <path id="lidFlap" d="M415,20 H1085 V55 C1190,55 1237,95 1237,140 C1237,172 1222,186 1085,188 V205 H415 V188 C278,186 263,172 263,140 C263,95 310,55 415,55 Z"/>
    <path id="lidPanel" d="M435,205 H1068 V665 H435 Z"/>
    <path id="lidSideLeft" d="M436,212 L300,262 C276,270 265,282 265,302 V625 C265,643 278,650 300,650 L436,658 Z"/>
    <path id="lidSideRight" d="M1067,212 L1200,262 C1224,270 1235,282 1235,302 V625 C1235,643 1222,650 1200,650 L1067,658 Z"/>
    <path id="frontPanel" d="M415,665 H1093 V848 H415 Z"/>
    <rect id="frontTabLeft" x="243" y="680" width="190" height="152" rx="22"/>
    <rect id="frontTabRight" x="1075" y="680" width="183" height="152" rx="22"/>
    <path id="basePanel" d="M28,857 H200 L225,848 H1275 L1300,857 H1470 V1290 H1300 L1275,1297 H225 L200,1290 H28 Z"/>
    <path id="baseNotchLeft" d="M30,1000 L16,1008 C11,1012 10,1016 10,1021 V1124 C10,1129 13,1133 18,1136 L30,1140 Z"/>
    <path id="baseNotchRight" d="M1468,1000 L1482,1008 C1487,1012 1490,1016 1490,1021 V1124 C1490,1129 1487,1133 1482,1136 L1468,1140 Z"/>
    <path id="bottomFlap" d="M425,1297 H1075 V1478 H425 Z"/>
    <rect id="bottomEarLeft" x="243" y="1310" width="205" height="157" rx="22"/>
    <rect id="bottomEarRight" x="1052" y="1310" width="205" height="157" rx="22"/>
  </defs>

  <g class="panel-outline">
    <use href="#lidFlap"/><use href="#lidSideLeft"/><use href="#lidSideRight"/><use href="#lidPanel"/>
    <use href="#frontTabLeft"/><use href="#frontTabRight"/><use href="#frontPanel"/>
    <use href="#baseNotchLeft"/><use href="#baseNotchRight"/><use href="#basePanel"/>
    <use href="#bottomEarLeft"/><use href="#bottomEarRight"/><use href="#bottomFlap"/>
  </g>

  <g class="panel-fill" role="img" aria-label="Soft lilac-to-sky-blue leaf and vine pattern covering the box">
    <use href="#lidFlap"/><use href="#lidSideLeft"/><use href="#lidSideRight"/><use href="#lidPanel"/>
    <use href="#frontTabLeft"/><use href="#frontTabRight"/><use href="#frontPanel"/>
    <use href="#baseNotchLeft"/><use href="#baseNotchRight"/><use href="#basePanel"/>
    <use href="#bottomEarLeft"/><use href="#bottomEarRight"/><use href="#bottomFlap"/>
  </g>

  <g class="ribbon lid-ribbon">
    <rect class="band" x="265" y="405" width="970" height="60"/>
    <line class="band-dots" x1="270" y1="398" x2="1232" y2="398"/>
    <line class="band-dots" x1="270" y1="472" x2="1232" y2="472"/>
  </g>
  <g class="ribbon base-ribbon">
    <rect class="band" x="10" y="1042" width="1480" height="61"/>
    <line class="band-dots" x1="15" y1="1035" x2="1487" y2="1035"/>
    <line class="band-dots" x1="15" y1="1109" x2="1487" y2="1109"/>
  </g>

  <g class="folds">
    <line class="fold" x1="415" y1="22" x2="415" y2="190"/>
    <line class="fold" x1="1085" y1="22" x2="1085" y2="190"/>
    <line class="fold" x1="435" y1="205" x2="1068" y2="205"/>
    <line class="fold" x1="435" y1="205" x2="435" y2="665"/>
    <line class="fold" x1="1068" y1="205" x2="1068" y2="665"/>
    <line class="fold" x1="415" y1="665" x2="1093" y2="665"/>
    <line class="fold" x1="415" y1="665" x2="415" y2="847"/>
    <line class="fold" x1="1093" y1="665" x2="1093" y2="847"/>
    <line class="fold" x1="405" y1="848" x2="1097" y2="848"/>
    <line class="fold" x1="405" y1="848" x2="405" y2="1297"/>
    <line class="fold" x1="1097" y1="848" x2="1097" y2="1297"/>
    <line class="fold" x1="405" y1="1297" x2="1097" y2="1297"/>
    <line class="fold" x1="425" y1="1297" x2="425" y2="1478"/>
    <line class="fold" x1="1075" y1="1297" x2="1075" y2="1478"/>
    <line class="crease" x1="203" y1="850" x2="203" y2="1295"/>
    <line class="crease" x1="225" y1="848" x2="225" y2="1297"/>
    <line class="crease" x1="1275" y1="848" x2="1275" y2="1297"/>
    <line class="crease" x1="1297" y1="850" x2="1297" y2="1295"/>
    <rect class="slot" x="402" y="1005" width="22" height="135"/>
    <rect class="slot" x="1075" y="1005" width="22" height="135"/>
  </g>

  <!-- lid artwork, printed upside down -->
  <g class="lid-artwork" transform="rotate(180 750 330)">
    <text class="script brand-name" x="745" y="242" text-anchor="middle">tovarin</text>
    <text class="script product-title" x="750" y="334" text-anchor="middle" textLength="290" lengthAdjust="spacingAndGlyphs">Cupboard Lock</text>
    <line class="rule" x1="605" y1="347" x2="895" y2="347"/>
    <text class="script tagline" x="749" y="373" text-anchor="middle" textLength="288" lengthAdjust="spacingAndGlyphs">#1 in Childproofing Your Home</text>
    <text class="script tagline" x="750" y="398" text-anchor="middle" textLength="165" lengthAdjust="spacingAndGlyphs">100% Money Back</text>
  </g>

  <g class="front-copy-block">
    <text class="script front-copy-de" text-anchor="middle">
      <tspan x="754" y="695" textLength="652" lengthAdjust="spacingAndGlyphs">"Text1:Das ist englische Text und es gibt nicht viel mehr als diese Zeichen sein, aber auch</tspan>
      <tspan x="752" y="717" textLength="511" lengthAdjust="spacingAndGlyphs">dort wird die deutsche Übersetzung in diesem gleichen Raum zu sein "</tspan>
      <tspan x="751" y="739" textLength="647" lengthAdjust="spacingAndGlyphs">"Text2:Vielleicht dieser Text auch insgesamt 300 englischen Zeichen Maximum auf ganze</tspan>
    </text>
    <text class="script front-copy" text-anchor="middle">
      <tspan x="752" y="771" textLength="659" lengthAdjust="spacingAndGlyphs">"Text1: This is English text and there will not be much more than these characters, but also</tspan>
      <tspan x="751" y="792" textLength="377" lengthAdjust="spacingAndGlyphs">there will be German translation in this same space"</tspan>
      <tspan x="752" y="813" textLength="665" lengthAdjust="spacingAndGlyphs">"Text2: Maybe this text too, overall 300 English characters maximum on whole package and</tspan>
      <tspan x="752" y="834" textLength="66" lengthAdjust="spacingAndGlyphs">that's it"</tspan>
    </text>
  </g>

  <g class="installation installation-en">
    <text class="script install-heading" x="583" y="1135" text-anchor="middle" textLength="67" lengthAdjust="spacingAndGlyphs">Installation</text>
    <text class="script install-en" text-anchor="middle">
      <tspan x="584" y="1153" textLength="305" lengthAdjust="spacingAndGlyphs">Make sure installation surfaces are clean. Position</tspan>
      <tspan x="583" y="1170" textLength="291" lengthAdjust="spacingAndGlyphs">the lock and latch very gently without using much</tspan>
      <tspan x="577" y="1187" textLength="326" lengthAdjust="spacingAndGlyphs">force, carefully check that lock and latch aligns with</tspan>
      <tspan x="584" y="1204" textLength="302" lengthAdjust="spacingAndGlyphs">each others perfectly, when you are happy with the</tspan>
      <tspan x="584" y="1221" textLength="289" lengthAdjust="spacingAndGlyphs">alignment firmly push adhesive surfaces in place</tspan>
      <tspan x="583" y="1238" textLength="303" lengthAdjust="spacingAndGlyphs">and leave for 24 hours for long-lasting and strong</tspan>
      <tspan x="583" y="1255" textLength="283" lengthAdjust="spacingAndGlyphs">installation. Easy to remove without leaving any</tspan>
      <tspan x="577" y="1272" textLength="332" lengthAdjust="spacingAndGlyphs">marks. Maximum effective thickness between lock and</tspan>
      <tspan x="583" y="1289" textLength="310" lengthAdjust="spacingAndGlyphs">key is 38mm. Standard drawer is usually 17-23mm.</tspan>
    </text>
  </g>
  <line class="column-divider" x1="750" y1="1140" x2="750" y2="1275"/>
  <g class="installation installation-de">
    <text class="script install-heading" x="920" y="1136" text-anchor="middle" textLength="60" lengthAdjust="spacingAndGlyphs">Installation</text>
    <text class="script install-de" text-anchor="middle">
      <tspan x="919" y="1153" textLength="312" lengthAdjust="spacingAndGlyphs">Stellen Sie sicher, Einbauflächen sauber sind. Positionieren</tspan>
      <tspan x="919" y="1169" textLength="309" lengthAdjust="spacingAndGlyphs">Sie das Schloss und Riegel ganz sanft , ohne viel Kraft ,</tspan>
      <tspan x="920" y="1185" textLength="323" lengthAdjust="spacingAndGlyphs">sorgfältig prüfen, Verriegelung und Riegel deckt sich mit der</tspan>
      <tspan x="920" y="1201" textLength="304" lengthAdjust="spacingAndGlyphs">jeweils anderen perfekt , wenn Sie zufrieden sind mit der</tspan>
      <tspan x="919" y="1217" textLength="321" lengthAdjust="spacingAndGlyphs">Ausrichtung fest drücken Klebeflächen an Ort und Stelle und</tspan>
      <tspan x="920" y="1233" textLength="317" lengthAdjust="spacingAndGlyphs">lassen für 24 Stunden für langanhaltende und starke Mon-</tspan>
      <tspan x="919" y="1249" textLength="318" lengthAdjust="spacingAndGlyphs">tage. Leicht zu rückstandslos entfernen. Maximale effektive</tspan>
      <tspan x="920" y="1265" textLength="316" lengthAdjust="spacingAndGlyphs">Dicke zwischen Schloss und Schlüssel ist 38mm . Standard-</tspan>
      <tspan x="919" y="1281" textLength="198" lengthAdjust="spacingAndGlyphs">Schublade ist in der Regel 17-23mm .</tspan>
    </text>
  </g>
</svg>
</body>
</html>
```